Business Card Design Project

Hello Designers, hope you are all aiming enjoy the weekend
I have the Business Logo (uploaded), you can alter the color which ever way you think would work,
Im looking for a simple yet striking feel, something which will stay memorable (I have uploaded 3 examples for you to flick through)
Information on the card, will just be the bare minimum,
Double Sided
Info being
i.e.
Name
Number
Website
ABN
Tobin Wexmoor
+468213579 (singapore)
+315792846 (Australia)
+729384615 (America)
www.lomevu-linkup.example
ABN 86420913
Enjoy,
Tobin
Industry/Entity Type
Business
Look and feel
Each slider illustrates characteristics of the customer's brand and the style your logo design should communicate.

```html
<!DOCTYPE html>
<html lang="en">
<head>
<meta charset="utf-8">
<title>Lomevu Linkup – Business Cards</title>
<link rel="stylesheet" href="https://fonts.googleapis.com/css2?family=Arimo:wght@400;700&display=swap">
<style>
  :root {
    --backdrop: #3a3a3a;
    --card-dark: #1f1f1f;
    --card-mid: #2c2c2c;
    --teal: #1fb3c4;
    --white: #ffffff;
    --divider: #5a5a5a;
  }
  * { margin: 0; padding: 0; box-sizing: border-box; }
  html, body { width: 1200px; height: 534px; overflow: hidden; }
  body {
    position: relative;
    background: var(--backdrop);
    font-family: "Arimo", Arial, sans-serif;
  }
  .card {
    position: absolute;
    top: 119px;
    width: 518px;
    height: 295px;
    border-radius: 16px;
    overflow: hidden;
    box-shadow: 0 4px 14px rgba(0,0,0,0.45);
  }
  .card--front { left: 59px; }
  .card--back { left: 625px; }
  .card-texture {
    position: absolute;
    inset: 0;
    background: radial-gradient(ellipse at 75% 20%, var(--card-mid) 0%, var(--card-dark) 70%);
  }
  .brand {
    position: absolute;
    display: flex;
    align-items: center;
    gap: 10px;
    color: var(--teal);
    font-weight: 700;
    white-space: nowrap;
  }
  .brand-dot {
    border-radius: 50%;
    background: var(--teal);
    flex: none;
  }
  .card--front .brand {
    left: 0; right: 0;
    top: 112px;
    justify-content: center;
    font-size: 40px;
  }
  .card--front .brand-dot { width: 34px; height: 34px; }
  .card--back .brand {
    left: 30px;
    top: 128px;
    font-size: 24px;
    gap: 8px;
  }
  .card--back .brand-dot { width: 26px; height: 26px; }
  .website {
    position: absolute;
    left: 0; right: 0;
    top: 216px;
    text-align: center;
    color: var(--white);
    font-weight: 700;
    font-size: 20px;
  }
  .divider {
    position: absolute;
    left: 261px;
    top: 114px;
    width: 1px;
    height: 68px;
    background: var(--divider);
  }
  .contact {
    position: absolute;
    left: 275px;
    top: 114px;
    line-height: 1.05;
  }
  .contact-name {
    color: var(--teal);
    font-weight: 700;
    font-size: 14px;
    letter-spacing: 0.5px;
    margin-bottom: 3px;
  }
  .contact-line {
    font-size: 11.5px;
    font-weight: 700;
    color: var(--white);
  }
  .contact-label {
    color: var(--teal);
    font-size: 10px;
    margin-right: 4px;
  }
</style>
</head>
<body>
  <section class="card card--front">
    <div class="card-texture" role="img" aria-label="Dark background texture of layered squares"></div>
    <div class="brand"><span class="brand-dot"></span>Lomevu Linkup</div>
    <p class="website">www.lomevu-linkup.example</p>
  </section>

  <section class="card card--back">
    <div class="card-texture" role="img" aria-label="Dark background texture of layered squares"></div>
    <div class="brand"><span class="brand-dot"></span>Lomevu Linkup</div>
    <div class="divider"></div>
    <div class="contact">
      <p class="contact-name">TOBIN WEXMOOR</p>
      <p class="contact-line"><span class="contact-label">SINGAPORE:</span>+46.821.3579</p>
      <p class="contact-line"><span class="contact-label">AUSTRALIA:</span>+31.579.2846</p>
      <p class="contact-line"><span class="contact-label">AMERICA:</span>+72.938.4615</p>
      <p class="contact-line"><span class="contact-label">ABN:</span>86420913</p>
    </div>
    <p class="website">www.lomevu-linkup.example</p>
  </section>
</body>
</html>
```